WebDesign | Financial Services Firm - Risk Mitigation

We are a professional services consulting firm that specializes in high net worth individuals over $25,000,000, executives C-suite and above, closely held businesses owners, family offices and highly compensated employees.

Our focus is on risk mitigation and tax efficient strategies. Our clients take their risk on themselves and have a proven track record generating wealth. Our directive is to preserve and protect the wealth they’ve already created.

Our company Harbinger Collective is geared around five directives of asset protection:
1) Legal Structuring
2) Leverage & Financing
3) Risk Management - Asset Protection & Insurance, Trustee Work
4) Asset Management & Investing - Under www.dvkfarcoast.com
5) Tax Efficient Strategies

Our Company Mark is a Pentagon with a key in the middle. A pentagon is the most efficient defensive structure. Each point of a pentagon is equal distance front every point . Each side provides support to another and works together, which is the key to our clients success.

Our key colors are blue, black and silver.

We ‘re located in the Pacific Northwest with bi coastal and international clients. We have fewer, higher net worth clients and provide exceptional customer service. We do not do social media.

We'll need the following pages:
-Front Landing Page.
Front page has to have link to hcportal.filevaultly.net for logging into secure site.
- Contact & About Us Page
- Our Team Page
- Five Sides of Wealth Management
> Legal & Business Structuring
> Leverage & Financing
> Risk Management & Asset Protection.
> Asset Management and Investing - Will link to DVK (won't be turned on for a few months)
> Tax Efficient Strategies.

Industry/Entity Type

Financial Service

Coding

Coded - Design and coding required

Number of Pages Required

5+ page

Font styles to use
Sans Serif

Colors
0555a3

Requirements
Must have
• Our key colors are blue, black and silver.

-Front Landing Page.
- Contact & About Us Page
- Our Team Page
> Leverage & Financing
Nice to have
• I have attached images that have been purchased for use on the webpage. Us or not.

location page: 872 W Birchwood Ave, Suite 114, Lake Oswego, OR 97035
Should not have
• lots of color.

```html
<!DOCTYPE html>
<html lang="en">
<head>
<meta charset="utf-8">
<title>Harbinger Collective</title>
<link href="https://fonts.googleapis.com/css2?family=Cinzel:wght@400;600;700&family=Lato:wght@400;700;900&family=Oswald:wght@500&display=swap" rel="stylesheet">
<style>
:root{
  --blue:#0555a3;
  --blue-deep:#0a4591;
  --blue-mid:#1460b4;
  --navy:#0b2f6b;
  --ink:#111;
  --text:#555;
  --silver:#c9ced6;
  --light:#f5f5f5;
  --white:#fff;
  --footer:#1f1f1f;
}
*{margin:0;padding:0;box-sizing:border-box}
html,body{width:1200px;height:4630px;overflow:hidden}
body{position:relative;font-family:"Lato",sans-serif;color:var(--text);background:var(--white)}
.abs{position:absolute}
section{position:absolute;left:0;width:1200px;overflow:hidden}

/* brand */
.brand{display:flex;align-items:center;gap:14px;color:var(--white);font-family:"Cinzel",serif;font-weight:600;font-size:24px;line-height:26px;letter-spacing:1px}
.brand .dot{width:52px;height:52px;border-radius:50%;border:3px solid var(--white);flex:none}

/* header + hero */
.hero{top:0;height:602px;background:linear-gradient(180deg,#2f4a6b 0%,#4a6078 30%,#5d5d50 62%,#6e5e49 100%)}
.hero-photo{position:absolute;inset:0;background:
  radial-gradient(ellipse 30% 22% at 60% 68%,rgba(214,168,96,.55),transparent 70%),
  radial-gradient(ellipse 22% 26% at 18% 82%,rgba(150,150,145,.5),transparent 70%),
  linear-gradient(90deg,rgba(18,32,58,.6),rgba(18,32,58,.12) 60%,rgba(18,32,58,.4))}
.hero .brand{left:95px;top:10px}
.phone{left:718px;top:16px;color:var(--white);font-size:15px;display:flex;align-items:center;gap:6px}
.nav{top:54px;left:452px;color:var(--white);font-size:15px;font-weight:700}
.nav a{color:var(--white);text-decoration:none;position:absolute;white-space:nowrap}
.nav a.active{border-bottom:2px solid var(--white);padding-bottom:2px}
.hero-title{left:151px;top:236px;color:var(--white);font-family:"Cinzel",serif;font-size:44px;font-weight:600;white-space:nowrap}
.hero-text{left:153px;top:296px;width:460px;color:var(--white);font-size:15px;line-height:27px;font-weight:700}
.btn-pill{display:flex;align-items:center;justify-content:center;border-radius:30px;background:var(--blue);color:var(--white);font-weight:700;font-size:15px;text-transform:uppercase}
.hero .btn-pill{left:147px;top:397px;width:185px;height:41px}
.slide-arrow{width:38px;height:38px;border-radius:50%;border:1.5px solid rgba(255,255,255,.8);top:304px}
.slide-arrow svg{display:block;margin:8px}
.slide-bars{left:515px;top:557px;display:flex;gap:10px}
.slide-bars span{width:38px;height:3px;background:rgba(255,255,255,.6)}
.slide-bars span.on{background:var(--blue-mid)}

/* solutions */
.solutions{top:602px;height:844px;background:linear-gradient(160deg,#1c63b7 0%,#0d52a4 50%,#0a4896 100%)}
.sol-head{left:111px;top:150px;color:var(--white);font-family:"Cinzel",serif;font-size:33px;font-weight:600}
.sol-intro{left:111px;top:202px;width:310px;color:var(--white);font-size:14px;line-height:28px}
.pent{width:348px;height:332px;color:var(--white);text-align:center}
.pent svg.frame{position:absolute;left:0;top:0}
.pent svg.icon{position:absolute;left:146px;top:30px}
.pent h3{position:absolute;left:30px;right:30px;top:118px;font-size:19px;font-weight:700;line-height:26px}
.pent p{position:absolute;left:48px;right:48px;top:153px;font-size:12.5px;line-height:26px}
.pent .more{position:absolute;left:0;right:0;top:278px;font-size:14px;font-weight:700;text-decoration:underline}

/* about */
.about{top:1446px;height:530px;background:var(--white)}
.mark{left:140px;top:78px;width:380px;height:380px;border-radius:50%;background:linear-gradient(160deg,#e9eef6,#cdd7e6);display:flex;align-items:center;justify-content:center;color:var(--navy);font-weight:900;font-size:34px;text-align:center;line-height:44px}
.about-label{left:622px;top:72px;color:var(--ink);font-size:17px;font-weight:700}
.about-name{left:621px;top:102px;color:var(--ink);font-family:"Cinzel",serif;font-size:39px;font-weight:700}
.about-text{left:621px;top:162px;width:467px;font-size:14px;line-height:27px;text-align:justify}
.about .btn-pill{left:623px;top:408px;width:182px;height:46px;background:var(--blue-deep)}

/* people */
.people{top:1976px;height:503px;background:var(--light)}
.section-title{left:0;width:1200px;text-align:center;color:var(--ink);font-family:"Cinzel",serif;font-size:36px;font-weight:700}
.person{top:153px;width:232px;height:271px;background:
  radial-gradient(ellipse 30% 40% at 50% 55%,rgba(40,60,95,.75),transparent 70%),
  linear-gradient(180deg,#b7c3d1,#7f93ab 45%,#3e5575)}
.person .band{position:absolute;left:0;right:0;top:165px;height:68px;background:rgba(5,85,163,.55);color:var(--white);text-align:center}
.person .band b{display:block;margin-top:12px;font-size:18px}
.person .band span{font-size:14px}
.person .cta{position:absolute;left:0;right:0;bottom:0;height:38px;background:var(--blue);color:var(--white);font-weight:700;font-size:15px;display:flex;align-items:center;justify-content:center;gap:6px}

/* reviews */
.reviews{top:2479px;height:535px;background:linear-gradient(180deg,#0d52a4,#0a4a98)}
.reviews .section-title{color:var(--white);top:86px}
.rev-sub{left:0;width:1200px;top:136px;text-align:center;color:var(--white);font-family:"Oswald",sans-serif;font-size:14px}
.review{top:224px;width:459px;height:196px;background:var(--white)}
.review p{position:absolute;left:14px;top:26px;width:430px;font-size:15px;line-height:28px;color:#666}
.review b{position:absolute;left:16px;top:118px;color:var(--ink);font-size:16px;font-weight:700}
.review small{position:absolute;left:16px;top:144px;font-size:14px;color:#666}
.review .quote{position:absolute;left:402px;top:128px;color:var(--blue);font-family:"Cinzel",serif;font-size:70px;font-weight:700;line-height:60px}
.avatar{top:180px;width:80px;height:80px;border-radius:50%;border:3px solid var(--white);background:linear-gradient(180deg,#c5ced9,#7d8ea5 55%,#3c4f6c)}
.rev-arrow{left:20px;top:306px;width:40px;height:40px;border-radius:50%;border:2px solid var(--white)}
.rev-arrow svg{display:block;margin:8px}
.dots{left:550px;top:446px;display:flex;gap:5px}
.dots span{width:11px;height:11px;border-radius:50%;background:#b8c9e2}
.dots span.on{background:var(--white)}

/* news */
.news{top:3014px;height:727px;background:var(--white)}
.news .section-title{top:74px}
.ph{background:linear-gradient(150deg,#c3ccd7,#7b8ba1 45%,#34435b)}
.ph.warm{background:linear-gradient(150deg,#d6d8dc,#9aa3ae 50%,#566273)}
.date{font-size:14px;color:var(--ink);display:flex;align-items:center;gap:5px}
.date i{width:11px;height:11px;background:var(--blue);display:inline-block}
.news-main-title{left:110px;top:500px;width:480px;color:var(--ink);font-size:18.5px;font-weight:700;line-height:29px}
.news-main-text{left:110px;top:560px;width:480px;font-size:12.5px;line-height:29px;color:#777}
.news-sm-title{width:240px;color:var(--ink);font-size:14.5px;font-weight:700;line-height:27px}

/* contact */
.contact{top:3741px;height:519px;background:linear-gradient(165deg,#0f56a8,#0a4a98)}
.contact-label{left:110px;top:175px;color:var(--white);font-size:18px}
.contact-head{left:110px;top:226px;width:380px;color:var(--white);font-family:"Cinzel",serif;font-size:31px;font-weight:700;line-height:47px}
.field{background:var(--white);border:1px solid #d8dde5;font-size:12.5px;color:#888;padding:0 12px;display:flex;align-items:center;justify-content:space-between}
.field.area{align-items:flex-start;padding-top:18px}
.send{left:492px;top:384px;width:264px;height:51px;border:2px solid var(--white);color:var(--white);font-weight:700;font-size:15px;display:flex;align-items:center;justify-content:center}

/* footer */
.footer{top:4260px;height:370px;background:var(--footer);color:var(--white)}
.footer .brand{left:111px;top:100px;font-size:22px;line-height:24px}
.footer .brand .dot{width:46px;height:46px}
.f-head{top:76px;font-size:17px;font-weight:700}
.f-list{font-size:14px;line-height:25.5px}
.f-item{font-size:14px;display:flex;gap:10px;align-items:flex-start;line-height:25px}
.sub-input{left:862px;top:164px;width:223px;height:43px;background:var(--white);color:#777;font-size:13px;display:flex;align-items:center;padding-left:14px}
.sub-input span{position:absolute;right:0;top:0;width:43px;height:43px;background:var(--blue);display:flex;align-items:center;justify-content:center}
.f-rule{left:110px;top:282px;width:980px;height:1px;background:#3a3a3a}
.f-bottom{top:303px;font-size:13px}
</style>
</head>
<body>

<section class="hero">
  <div class="hero-photo" role="img" aria-label="Photo of a timber-roofed office building at dusk with a stone fountain in front"></div>
  <div class="abs brand"><span class="dot"></span><span>Harbinger<br>Collective</span></div>
  <div class="abs phone">
    <svg width="14" height="14" viewBox="0 0 24 24"><path fill="#fff" d="M6.6 10.8a15.1 15.1 0 0 0 6.6 6.6l2.2-2.2c.3-.3.7-.4 1-.2 1.1.4 2.3.6 3.6.6.6 0 1 .4 1 1V20c0 .6-.4 1-1 1A17 17 0 0 1 3 4c0-.6.4-1 1-1h3.5c.6 0 1 .4 1 1 0 1.3.2 2.5.6 3.6.1.3 0 .7-.2 1z"/></svg>
    Phone: (+1) 555 014 2290
  </div>
  <nav class="abs nav">
    <a class="active" style="left:0">Home</a>
    <a style="left:90px">About Us</a>
    <a style="left:195px">Our Solutions</a>
    <a style="left:333px">Our Team</a>
    <a style="left:448px">Partners</a>
    <a style="left:554px">Contact Us</a>
  </nav>
  <h1 class="abs hero-title">Harbinger Collective</h1>
  <p class="abs hero-text">Lorem ipsum dolor sit amet, consectetur adipiscing elit, sed do eiusmod tempor incididunt ut labore et dolore magna aliqua. Ut enim ad minim veniam,</p>
  <div class="abs btn-pill">File Share</div>
  <div class="abs slide-arrow" style="left:46px"><svg width="20" height="20" viewBox="0 0 20 20"><path d="M12 4 6 10l6 6" stroke="#fff" stroke-width="1.6" fill="none"/></svg></div>
  <div class="abs slide-arrow" style="left:1109px"><svg width="20" height="20" viewBox="0 0 20 20"><path d="M8 4l6 6-6 6" stroke="#fff" stroke-width="1.6" fill="none"/></svg></div>
  <div class="abs slide-bars"><span class="on"></span><span></span><span></span><span></span></div>
</section>

<section class="solutions">
  <h2 class="abs sol-head">Our Solutions</h2>
  <p class="abs sol-intro">Lorem ipsum dolor sit amet, conr adipiscing elit, sed do eiusmod tempor incidt ut labore et dolore maga aiqua. Is ipsum suspendisse ultrices gravida. comodo viverra maecenas accumsan lacus vel facilisis.</p>

  <div class="abs pent" style="left:426px;top:77px">
    <svg class="frame" width="348" height="332" viewBox="0 0 348 332"><polygon points="174,2 346,127 280,330 68,330 2,127" fill="none" stroke="#fff" stroke-width="1.5"/></svg>
    <svg class="icon" width="56" height="60" viewBox="0 0 56 60" fill="none" stroke="#fff" stroke-width="2"><rect x="6" y="4" width="34" height="46" rx="3"/><path d="M14 16h18M14 24h18M14 32h12"/><circle cx="42" cy="44" r="9"/><path d="M38 52l-2 7 6-3 6 3-2-7"/></svg>
    <h3>Legal &amp; Business Structuring</h3>
    <p>Lorem ipsum dolor sit onsectetur adipiscing elit, sed eiusmod temr incididunt ut labore et dolore magna aliqua. Ut enim ad minim veniam, quis nostrud exercitation</p>
    <span class="more">READ MORE &gt;&gt;</span>
  </div>
  <div class="abs pent" style="left:792px;top:77px">
    <svg class="frame" width="348" height="332" viewBox="0 0 348 332"><polygon points="174,2 346,127 280,330 68,330 2,127" fill="none" stroke="#fff" stroke-width="1.5"/></svg>
    <svg class="icon" width="56" height="60" viewBox="0 0 56 60" fill="none" stroke="#fff" stroke-width="2"><circle cx="18" cy="42" r="13"/><path d="M18 34v16M22 37h-6a2.5 2.5 0 0 0 0 5h4a2.5 2.5 0 0 1 0 5h-6"/><ellipse cx="42" cy="48" rx="10" ry="4"/><ellipse cx="42" cy="40" rx="10" ry="4"/><path d="M34 22v14M34 22c-6-2-8-8-8-12 6 0 8 6 8 12zM34 26c6-2 9-8 9-13-6 1-9 7-9 13z"/></svg>
    <h3>Leverage &amp; Financing</h3>
    <p>Lorem ipsum dolor sit onsectetur adipiscing elit, sed eiusmod temr incididunt ut labore et dolore magna aliqua. Ut enim ad minim veniam, quis nostrud exercitation</p>
    <span class="more">READ MORE &gt;&gt;</span>
  </div>
  <div class="abs pent" style="left:58px;top:422px">
    <svg class="frame" width="348" height="332" viewBox="0 0 348 332"><polygon points="174,2 346,127 280,330 68,330 2,127" fill="none" stroke="#fff" stroke-width="1.5"/></svg>
    <svg class="icon" width="56" height="60" viewBox="0 0 56 60" fill="none" stroke="#fff" stroke-width="2"><path d="M4 50h14l10 4 18-8-4-4-14 4"/><path d="M18 50v-6l10-2h8"/><path d="M20 34v-8M30 34V20M40 34V14M48 34V10"/><path d="M16 22l12-10 8 6 14-12"/></svg>
    <h3>Risk Management &amp; Asset Protection</h3>
    <p style="top:180px">Lorem ipsum dolor sit onsectetur adipiscing elit, sed eiusmod temr incididunt ut labore et dolore magna aliqua. Ut enim</p>
    <span class="more">READ MORE &gt;&gt;</span>
  </div>
  <div class="abs pent" style="left:426px;top:422px">
    <svg class="frame" width="348" height="332" viewBox="0 0 348 332"><polygon points="174,2 346,127 280,330 68,330 2,127" fill="none" stroke="#fff" stroke-width="1.5"/></svg>
    <svg class="icon" width="56" height="60" viewBox="0 0 56 60" fill="none" stroke="#fff" stroke-width="2"><rect x="6" y="8" width="14" height="16" rx="2"/><path d="M13 12v8M16 14h-4a1.5 1.5 0 0 0 0 3h2a1.5 1.5 0 0 1 0 3h-4"/><circle cx="38" cy="18" r="10"/><path d="M38 12v6l4 3"/><path d="M4 52h14l10 4 18-8-4-4-14 4"/><path d="M18 52v-6l10-2h8"/></svg>
    <h3>Asset Management &amp; Investing</h3>
    <p>Lorem ipsum dolor sit onsectetur adipiscing elit, sed eiusmod temr incididunt ut labore et dolore magna aliqua. Ut enim ad minim veniam, quis nostrud exercitation</p>
    <span class="more">READ MORE &gt;&gt;</span>
  </div>
  <div class="abs pent" style="left:792px;top:422px">
    <svg class="frame" width="348" height="332" viewBox="0 0 348 332"><polygon points="174,2 346,127 280,330 68,330 2,127" fill="none" stroke="#fff" stroke-width="1.5"/></svg>
    <svg class="icon" width="56" height="60" viewBox="0 0 56 60" fill="none" stroke="#fff" stroke-width="2"><rect x="8" y="4" width="40" height="52" rx="3"/><path d="M8 20h40"/><path d="M14 28h12M14 35h12M14 42h10"/><path d="M32 44l10-12"/><circle cx="33" cy="33" r="2"/><circle cx="41" cy="43" r="2"/></svg>
    <h3>Tax Efficient Strategies</h3>
    <p>Lorem ipsum dolor sit onsectetur adipiscing elit, sed eiusmod temr incididunt ut labore et dolore magna aliqua. Ut enim ad minim veniam, quis nostrud exercitation</p>
    <span class="more">READ MORE &gt;&gt;</span>
  </div>
</section>

<section class="about">
  <div class="abs mark">Harbinger<br>Collective</div>
  <div class="abs about-label">ABOUT US</div>
  <h2 class="abs about-name">Garrett Ashdown</h2>
  <p class="abs about-text">Garrett Ashdown is the Financial Strategist and Founder who partners with C-Suite Executives, Family Offices, Real Estate Investors and Closely Held Business Owners to protect and maximize their wealth. After spending 15 years in the commercial banking and wealth management as a commercial and private lender Garrett developed a comprehensive approach to asset protection and wealth preservation. The comprehensive approach creates a plan that focuses on the client's income tax first with wealth preservation</p>
  <div class="abs btn-pill">Learn More</div>
</section>

<section class="people">
  <h2 class="abs section-title" style="top:80px">Meet Our People</h2>
  <div class="abs person" style="left:110px" role="img" aria-label="Portrait of a team member in a suit in an office">
    <div class="band"><b>Rowan Ellery</b><span>Lorem ipsum</span></div>
    <div class="cta">LEARN MORE <svg width="16" height="10" viewBox="0 0 16 10"><path d="M0 5h13M10 1l4 4-4 4" stroke="#fff" stroke-width="1.8" fill="none"/></svg></div>
  </div>
  <div class="abs person" style="left:357px" role="img" aria-label="Portrait of a team member on a city street">
    <div class="band"><b>Tobias Marke</b><span>Lorem ipsum</span></div>
    <div class="cta">LEARN MORE <svg width="16" height="10" viewBox="0 0 16 10"><path d="M0 5h13M10 1l4 4-4 4" stroke="#fff" stroke-width="1.8" fill="none"/></svg></div>
  </div>
  <div class="abs person" style="left:605px" role="img" aria-label="Portrait of a team member with a city skyline">
    <div class="band"><b>Emmett Varga</b><span>Lorem ipsum</span></div>
    <div class="cta">LEARN MORE <svg width="16" height="10" viewBox="0 0 16 10"><path d="M0 5h13M10 1l4 4-4 4" stroke="#fff" stroke-width="1.8" fill="none"/></svg></div>
  </div>
  <div class="abs person" style="left:853px" role="img" aria-label="Portrait of a team member in a bright office">
    <div class="band"><b>Lucas Brandt</b><span>Lorem ipsum</span></div>
    <div class="cta">LEARN MORE <svg width="16" height="10" viewBox="0 0 16 10"><path d="M0 5h13M10 1l4 4-4 4" stroke="#fff" stroke-width="1.8" fill="none"/></svg></div>
  </div>
</section>

<section class="reviews">
  <h2 class="abs section-title">Client Reviews</h2>
  <p class="abs rev-sub">Lorem ipsum dolor sit amet, consectetur adipiscing elit, sed do eiusmod tempor incididunt ut</p>
  <div class="abs review" style="left:92px">
    <p>Lorem ipsum dolor sit amet, consectetur adipiscing elit, sed do eiusmod tempor incididunt ut labore et dolore magna aliqua. Quis ipsum suspendisse</p>
    <b>Peter Hollis</b><small>Lorem ipsum dolor</small><span class="quote">&ldquo;</span>
  </div>
  <div class="abs review" style="left:566px">
    <p>Lorem ipsum dolor sit amet, consectetur adipiscing elit, sed do eiusmod tempor incididunt ut labore et dolore magna aliqua. Quis ipsum suspendisse</p>
    <b>Peter Hollis</b><small>Lorem ipsum dolor</small><span class="quote">&ldquo;</span>
  </div>
  <div class="abs review" style="left:1038px">
    <p>Lorem ipsum dolor sit amet, consectetur adipiscing elit, sed do eiusmod tempor incididunt ut labore et dolore magna aliqua. Quis ipsum suspendisse</p>
    <b>Peter Hollis</b><small>Lorem ipsum dolor</small><span class="quote">&ldquo;</span>
  </div>
  <div class="abs avatar" style="left:106px" role="img" aria-label="Client portrait"></div>
  <div class="abs avatar" style="left:576px" role="img" aria-label="Client portrait"></div>
  <div class="abs avatar" style="left:1048px" role="img" aria-label="Client portrait"></div>
  <div class="abs rev-arrow"><svg width="20" height="20" viewBox="0 0 20 20"><path d="M16 10H4M9 5l-5 5 5 5" stroke="#fff" stroke-width="1.8" fill="none"/></svg></div>
  <div class="abs dots"><span class="on"></span><span></span><span></span><span></span></div>
</section>

<section class="news">
  <h2 class="abs section-title">Latest News</h2>
  <div class="abs ph" style="left:110px;top:147px;width:474px;height:291px" role="img" aria-label="Business people reviewing charts on a laptop"></div>
  <div class="abs date" style="left:110px;top:462px"><i></i>15 April,2020</div>
  <h3 class="abs news-main-title">Lorem ipsum dolor sit amet, consectetur adipiscing elit, sed do eiusmod tempor</h3>
  <p class="abs news-main-text">Lorem ipsum dolor sit amet, consectetur adipiscineiusmod tempor incididunt ut labore et dolore magna aliqua. Quis ipsum pendisse ultrices gravida.Lorem ipsum dolor sit amet, consectetur adipiscineiusmod</p>

  <div class="abs ph" style="left:600px;top:147px;width:237px;height:144px" role="img" aria-label="Hands using a tablet with charts"></div>
  <div class="abs date" style="left:600px;top:305px"><i></i>15 April,2020</div>
  <h4 class="abs news-sm-title" style="left:600px;top:330px">Lorem ipsum dolorconsectetur adipiscing elit, sed do eiusmod</h4>
  <div class="abs ph warm" style="left:851px;top:147px;width:238px;height:144px" role="img" aria-label="Financial reports on a desk"></div>
  <div class="abs date" style="left:851px;top:305px"><i></i>15 April,2020</div>
  <h4 class="abs news-sm-title" style="left:851px;top:330px">Lorem ipsum dolorconsectetur adipiscing elit, sed do eiusmod</h4>

  <div class="abs ph warm" style="left:600px;top:407px;width:237px;height:144px" role="img" aria-label="Person working at a laptop"></div>
  <div class="abs date" style="left:600px;top:566px"><i></i>15 April,2020</div>
  <h4 class="abs news-sm-title" style="left:600px;top:592px">Lorem ipsum dolorconsectetur adipiscing elit, sed do eiusmod</h4>
  <div class="abs ph" style="left:851px;top:407px;width:238px;height:144px" role="img" aria-label="Colleagues discussing documents"></div>
  <div class="abs date" style="left:851px;top:566px"><i></i>15 April,2020</div>
  <h4 class="abs news-sm-title" style="left:851px;top:592px">Lorem ipsum dolorconsectetur adipiscing elit, sed do eiusmod</h4>
</section>

<section class="contact">
  <div class="abs contact-label">CONTACT US</div>
  <h2 class="abs contact-head">Don't Hesitate to Contact us for any Information.</h2>
  <div class="abs field" style="left:490px;top:86px;width:295px;height:49px">First Name</div>
  <div class="abs field" style="left:794px;top:86px;width:295px;height:49px">Last Name</div>
  <div class="abs field" style="left:490px;top:146px;width:295px;height:49px">Email</div>
  <div class="abs field" style="left:794px;top:146px;width:295px;height:49px">Phone</div>
  <div class="abs field" style="left:490px;top:206px;width:295px;height:49px">Select Service <svg width="9" height="6" viewBox="0 0 9 6"><path d="M0 0h9L4.5 6z" fill="#666"/></svg></div>
  <div class="abs field" style="left:794px;top:206px;width:295px;height:49px">Select Industry <svg width="9" height="6" viewBox="0 0 9 6"><path d="M0 0h9L4.5 6z" fill="#666"/></svg></div>
  <div class="abs field area" style="left:490px;top:266px;width:599px;height:101px">How Can We Help You</div>
  <div class="abs send">SEND US YOUR ENQUIRY</div>
</section>

<footer class="abs footer" style="left:0;width:1200px">
  <div class="abs brand"><span class="dot"></span><span>Harbinger<br>Collective</span></div>

  <div class="abs f-head" style="left:421px">QUICK LINKS</div>
  <div class="abs f-list" style="left:421px;top:107px">Home<br>About Us<br>Our Solutions<br>Our team<br>Contact Us</div>

  <div class="abs f-head" style="left:584px">CONTACT INFO</div>
  <div class="abs f-item" style="left:584px;top:107px">
    <svg width="13" height="17" viewBox="0 0 13 17" style="margin-top:5px"><path d="M6.5 1A5.5 5.5 0 0 0 1 6.5C1 11 6.5 16 6.5 16S12 11 12 6.5A5.5 5.5 0 0 0 6.5 1z" fill="none" stroke="#fff" stroke-width="1.3"/><circle cx="6.5" cy="6.5" r="2" fill="#fff"/></svg>
    <span>123 Avenue name, City name<br>10150, United States</span>
  </div>
  <div class="abs f-item" style="left:584px;top:167px">
    <svg width="14" height="14" viewBox="0 0 24 24" style="margin-top:5px"><path fill="#fff" d="M6.6 10.8a15.1 15.1 0 0 0 6.6 6.6l2.2-2.2c.3-.3.7-.4 1-.2 1.1.4 2.3.6 3.6.6.6 0 1 .4 1 1V20c0 .6-.4 1-1 1A17 17 0 0 1 3 4c0-.6.4-1 1-1h3.5c.6 0 1 .4 1 1 0 1.3.2 2.5.6 3.6.1.3 0 .7-.2 1z"/></svg>
    <span>555 014 2290</span>
  </div>
  <div class="abs f-item" style="left:584px;top:205px">
    <svg width="15" height="11" viewBox="0 0 15 11" style="margin-top:8px"><rect x=".6" y=".6" width="13.8" height="9.8" fill="none" stroke="#fff" stroke-width="1.2"/><path d="M.6.6l6.9 5.4L14.4.6" fill="none" stroke="#fff" stroke-width="1.2"/></svg>
    <span>info@harbingercollective.com</span>
  </div>

  <div class="abs f-head" style="left:862px">SUBSCRIBE NEWSLETTER</div>
  <div class="abs f-list" style="left:862px;top:104px;width:230px;font-size:13px;line-height:21px">Lorem ips sit amet, consectetur adipiscing elit, sed do</div>
  <div class="abs sub-input">email address<span><svg width="18" height="18" viewBox="0 0 24 24"><path d="M2 12 22 3l-6 18-4-7z" fill="none" stroke="#fff" stroke-width="1.8"/><path d="M12 14 22 3" stroke="#fff" stroke-width="1.8"/></svg></span></div>

  <div class="abs f-rule"></div>
  <div class="abs f-bottom" style="left:111px">Copyright &copy; 2020 Harbinger Collective.All Rights Reserved.</div>
  <div class="abs f-bottom" style="left:876px">Terms &amp;Conditions &nbsp;&nbsp;|&nbsp;&nbsp; Privacy Policy</div>
</footer>

</body>
</html>
```